Lantern Ridge Mentoring seeks to be a Guidance Counsellor to the World

Word Press site to be published to HostMarlo account on completion.

Basic site with integration wth Vellix Word Press Plug-in.

All simple pages to create are shown in attached power point.

LanternRidgeMentoring.com™️ seeks to be a Guidance Counsellor to the World. We help students by bringing high quality, interactive content to their virtual doorstep.

Target Market(s)

Careers

Coding

Coded - Design and coding required

Font styles to use
Sans Serif

Requirements
Must have
• Details are in powerpoint:
Registration to allow integration with Word Press Vellix Plug-in.
Nice to have
• Bright and modern feel

```html
<!DOCTYPE html>
<html lang="en">
<head>
<meta charset="utf-8">
<title>Lantern Ridge Mentoring – Page Layouts</title>
<link href="https://fonts.googleapis.com/css2?family=Nunito+Sans:wght@300;400;700;800&display=swap" rel="stylesheet">
<style>
  :root {
    --orange: #f7941d;
    --orange-deep: #ef7d22;
    --charcoal: #58595b;
    --ink: #3d3d3f;
    --white: #ffffff;
    --stage: #d3d3d3;
    --mist: #f4f4f4;
  }
  * { margin: 0; padding: 0; box-sizing: border-box; }
  html, body { width: 1200px; height: 917px; overflow: hidden; }
  body {
    background: var(--stage);
    font-family: "Nunito Sans", "Helvetica Neue", Arial, sans-serif;
    position: relative;
  }
  .screen {
    position: absolute;
    width: 552px;
    height: 409px;
    overflow: hidden;
    background: var(--white);
  }
  .screen--home-warm { left: 45px; top: 26px; }
  .screen--home-light { left: 617px; top: 26px; }
  .screen--mission { left: 45px; top: 463px; }

  .site-nav {
    position: absolute; left: 0; top: 0; width: 100%; height: 29px;
    display: flex; align-items: center; justify-content: center;
    color: var(--white); font-weight: 800; font-size: 10px;
  }
  .site-nav--dark { background: var(--charcoal); }
  .site-nav--orange { background: var(--orange); }
  .site-nav__item { position: relative; padding: 0 2px; line-height: 29px; }
  .site-nav__sep { margin: 0 18px; font-weight: 400; }
  .site-nav__item--active::after {
    content: ""; position: absolute; left: -2px; right: -2px; bottom: 0;
    height: 2px; background: var(--charcoal);
  }
  .site-nav__caret { display: inline-block; vertical-align: middle; margin-left: 3px; }

  .hero {
    position: absolute; left: 0; top: 29px; width: 100%; height: 347px;
  }
  .hero__photo { position: absolute; inset: 0; }
  .hero__photo--warm {
    background: linear-gradient(110deg, #ef7a22 0%, #f29a2e 40%, #f5b53a 75%, #f3ad36 100%);
  }
  .hero__photo--light {
    background: linear-gradient(110deg, #efefef 0%, #f7f7f7 45%, #f1f1f1 100%);
  }

  .brand {
    position: absolute; left: 0; width: 100%; text-align: center;
    display: flex; flex-direction: column; align-items: center;
  }
  .brand__dot { width: 26px; height: 26px; border-radius: 50%; margin-bottom: 8px; }
  .brand__name { font-weight: 700; font-size: 22px; letter-spacing: 0.2px; }

  .hero-title {
    position: absolute; left: 0; width: 100%; text-align: center;
    font-weight: 800; font-size: 23px;
  }

  .event-card {
    position: absolute; text-align: center; color: var(--white);
  }
  .event-card--framed {
    left: 170px; top: 180px; width: 212px; height: 97px;
    border: 1.5px solid var(--white); border-radius: 3px;
  }
  .event-card__title { font-weight: 800; font-size: 18px; line-height: 22px; }
  .event-card__line { font-weight: 300; font-size: 11.5px; line-height: 16px; }
  .event-card--framed .event-card__title { margin-top: 12px; }

  .event-card--diamond { left: 141px; top: 183px; width: 270px; height: 93px; }
  .event-card--diamond svg { position: absolute; inset: 0; }
  .event-card--diamond .event-card__body { position: relative; padding-top: 27px; }
  .event-card--diamond .event-card__line { font-weight: 400; font-size: 10.5px; line-height: 15px; }

  .register-btn {
    position: absolute; height: 27px; width: 94px; border-radius: 14px;
    font-weight: 800; font-size: 9.5px; line-height: 27px; text-align: center;
  }
  .register-btn--light { left: 232px; top: 261px; background: var(--white); color: var(--orange); }
  .register-btn--orange { left: 236px; top: 271px; background: var(--orange); color: var(--white); }

  .site-footer {
    position: absolute; left: 0; bottom: 0; width: 100%; height: 33px;
    font-size: 6.5px; text-align: center; line-height: 33px;
  }
  .site-footer--light { background: var(--white); color: var(--charcoal); }
  .site-footer--dark { background: var(--charcoal); color: var(--white); }

  .mission {
    position: absolute; left: 0; top: 0; width: 100%; text-align: center;
  }
  .mission__heading { font-weight: 800; font-size: 21px; color: var(--charcoal); margin-top: 140px; }
  .mission__heading span { color: var(--orange); }
  .mission__text {
    width: 420px; margin: 12px auto 0; font-weight: 400; font-size: 13.5px;
    line-height: 26px; color: var(--ink);
  }
</style>
</head>
<body>

  <!-- Home, warm variant -->
  <section class="screen screen--home-warm">
    <nav class="site-nav site-nav--dark">
      <span class="site-nav__item">Our Mission</span><span class="site-nav__sep">|</span>
      <span class="site-nav__item">Our Programs</span><span class="site-nav__sep">|</span>
      <span class="site-nav__item">Get Involved</span><span class="site-nav__sep">|</span>
      <span class="site-nav__item">+info<svg class="site-nav__caret" width="7" height="5" viewBox="0 0 7 5"><path d="M0.5 0.8 3.5 3.8 6.5 0.8" fill="none" stroke="#fff" stroke-width="1.2"/></svg></span>
    </nav>
    <div class="hero">
      <div class="hero__photo hero__photo--warm" role="img" aria-label="Students working together at a desk, tinted orange"></div>
      <div class="brand" style="top:40px;color:var(--white)">
        <span class="brand__dot" style="background:var(--white)"></span>
        <span class="brand__name">Lantern Ridge Mentoring</span>
      </div>
      <h1 class="hero-title" style="top:135px;color:var(--white)">The World’s Guidance Counsellor</h1>
      <div class="event-card event-card--framed">
        <p class="event-card__title">War on Viruses</p>
        <p class="event-card__line">Dr. Mara Quillan, phD</p>
        <p class="event-card__line">Senior Research Scientist</p>
      </div>
      <span class="register-btn register-btn--light">Register Now</span>
    </div>
    <footer class="site-footer site-footer--light">© 2020 Company Name | All Rights Reserved | Disclaimer</footer>
  </section>

  <!-- Home, light variant -->
  <section class="screen screen--home-light">
    <nav class="site-nav site-nav--orange">
      <span class="site-nav__item">Our Mission</span><span class="site-nav__sep">|</span>
      <span class="site-nav__item">Our Programs</span><span class="site-nav__sep">|</span>
      <span class="site-nav__item">Get Involved</span><span class="site-nav__sep">|</span>
      <span class="site-nav__item">+info<svg class="site-nav__caret" width="7" height="5" viewBox="0 0 7 5"><path d="M0.5 0.8 3.5 3.8 6.5 0.8" fill="none" stroke="#fff" stroke-width="1.2"/></svg></span>
    </nav>
    <div class="hero">
      <div class="hero__photo hero__photo--light" role="img" aria-label="Students working together at a desk, faded to white"></div>
      <div class="brand" style="top:40px;color:var(--charcoal)">
        <span class="brand__dot" style="background:var(--orange)"></span>
        <span class="brand__name">Lantern Ridge Mentoring</span>
      </div>
      <h1 class="hero-title" style="top:142px;color:var(--ink)">The World’s Guidance Counsellor</h1>
      <div class="event-card event-card--diamond">
        <svg width="270" height="93" viewBox="0 0 270 93"><polygon points="135,0 270,55 135,93 0,55" fill="#58595b"/></svg>
        <div class="event-card__body">
          <p class="event-card__title">War on Viruses</p>
          <p class="event-card__line">Dr. Mara Quillan, phD</p>
          <p class="event-card__line">Senior Research Scientist</p>
        </div>
      </div>
      <span class="register-btn register-btn--orange">Register Now</span>
    </div>
    <footer class="site-footer site-footer--dark">© 2020 Company Name | All Rights Reserved | Disclaimer</footer>
  </section>

  <!-- Our Mission page -->
  <section class="screen screen--mission">
    <nav class="site-nav site-nav--orange">
      <span class="site-nav__item site-nav__item--active">Our Mission</span><span class="site-nav__sep">|</span>
      <span class="site-nav__item">Our Programs</span><span class="site-nav__sep">|</span>
      <span class="site-nav__item">Get Involved</span><span class="site-nav__sep">|</span>
      <span class="site-nav__item">+info<svg class="site-nav__caret" width="7" height="5" viewBox="0 0 7 5"><path d="M0.5 0.8 3.5 3.8 6.5 0.8" fill="none" stroke="#fff" stroke-width="1.2"/></svg></span>
    </nav>
    <div class="hero">
      <div class="hero__photo hero__photo--light" role="img" aria-label="Students working together at a desk, faded to white"></div>
      <div class="brand" style="top:45px;color:var(--charcoal)">
        <span class="brand__dot" style="background:var(--orange)"></span>
        <span class="brand__name" style="font-size:14px">Lantern Ridge Mentoring</span>
      </div>
      <div class="mission" style="top:-29px">
        <h2 class="mission__heading">Our <span>Mission</span></h2>
        <p class="mission__text">LanternRidgeMentoring.com™ seeks to Contact be a Guidance Counsellor to the World. We help students by bringing high quality, interactive content to their virtual doorstep.</p>
      </div>
    </div>
    <footer class="site-footer site-footer--dark">© 2020 Company Name | All Rights Reserved | Disclaimer</footer>
  </section>

</body>
</html>
```